Business card design for Automotive workshop

We need a business card for a new automotive repair and tyre shop called Ridgeback Prime Automotive located in New Zealand. We are a clean, modern and fresh workshop and company.

Front needs to feature logo,
my name:
Lachie Westergaard (director)

Address:
48 Marlow Lane
Harlow Bay 3577

Phone: 07 842 1937
Mobile: 027 519 2764
Email: office@ridgebackmotors.co.nz
Website: ridgebackmotors.co.nz

Back needs to feature an area to write down appointment details, date and time.

Also feature a list of jobs and work we do such as,
Vehicle Servicing
All Mechanical Repairs
Warrant of Fitness
Tyres & Wheel Alignments
Automotive Diagnostics
Automotive Parts & Supplies

```html
<!DOCTYPE html>
<html lang="en">
<head>
<meta charset="utf-8">
<title>Ridgeback Prime Automotive – Business Card</title>
<link rel="stylesheet" href="https://fonts.googleapis.com/css2?family=Roboto:wght@400;500;700&display=swap">
<style>
  :root {
    --bg: #e9e7e5;
    --card-dark: #222222;
    --band-dark: #2a2a2a;
    --paper: #ffffff;
    --red: #e0202b;
    --ink: #1e1e1e;
    --muted: #d8d8d8;
    --rule: #9a9a9a;
  }
  * { box-sizing: border-box; margin: 0; padding: 0; }
  html, body { width: 1200px; height: 716px; overflow: hidden; }
  body {
    background: var(--bg);
    font-family: "Roboto", Arial, sans-serif;
    position: relative;
  }
  .card {
    position: absolute;
    top: 205px;
    width: 540px;
    height: 306px;
    box-shadow: 0 8px 24px rgba(0,0,0,.18);
    overflow: hidden;
  }
  .card--front { left: 40px; background: var(--card-dark); color: #fff; }
  .card--back { left: 620px; background: var(--paper); color: var(--ink); }

  .brand {
    position: absolute;
    left: 0; right: 0;
    text-align: center;
    color: var(--red);
    font-weight: 700;
    text-transform: uppercase;
  }
  .brand__name { font-size: 34px; letter-spacing: 2px; line-height: 1; }
  .brand__sub { font-size: 14px; letter-spacing: 6px; margin-top: 6px; }
  .card--front .brand { top: 48px; }
  .card--back .brand { top: 24px; }

  /* front */
  .person {
    position: absolute;
    right: 298px;
    top: 184px;
    text-align: right;
  }
  .person__name { color: var(--red); font-weight: 700; font-size: 20px; }
  .person__role { font-size: 12px; color: var(--muted); margin-top: 1px; }
  .person__address { font-size: 11.5px; color: var(--muted); margin-top: 12px; line-height: 1.35; }
  .divider {
    position: absolute;
    left: 262px; top: 188px;
    width: 1px; height: 86px;
    background: var(--muted);
  }
  .contact {
    position: absolute;
    left: 278px; top: 188px;
    list-style: none;
    font-size: 12px;
    color: var(--muted);
  }
  .contact li { display: flex; align-items: center; height: 19.5px; }
  .contact svg { width: 9px; height: 9px; margin-right: 5px; fill: var(--red); flex: none; }

  /* back */
  .appointment {
    position: absolute;
    top: 120px; left: 0; right: 0;
    text-align: center;
    color: var(--red);
    font-size: 19px;
    font-weight: 500;
  }
  .field-row {
    position: absolute;
    top: 181px; left: 30px; right: 28px;
    display: flex;
    gap: 8px;
    font-size: 15px;
  }
  .field { display: flex; align-items: flex-end; flex: 1; }
  .field__line { flex: 1; border-bottom: 1px solid var(--rule); margin-left: 3px; height: 14px; }
  .days {
    position: absolute;
    top: 216px; left: 78px; right: 70px;
    display: flex;
    justify-content: space-between;
    list-style: none;
    font-size: 14px;
  }
  .days li { display: flex; align-items: center; }
  .days li::before {
    content: "";
    width: 13px; height: 13px;
    border: 1.3px solid var(--red);
    border-radius: 50%;
    margin-right: 3px;
  }
  .services {
    position: absolute;
    left: 0; right: 0; bottom: 0;
    height: 48px;
    background: var(--band-dark);
    border-top: 3px solid var(--red);
    color: #fff;
    font-size: 11.2px;
    text-align: center;
    padding-top: 6px;
    line-height: 15px;
  }
  .services span::before { content: "• "; color: var(--red); }
  .services span { margin: 0 2px; }
</style>
</head>
<body>
  <section class="card card--front" aria-label="Card front">
    <div class="brand">
      <div class="brand__name">Ridgeback Prime</div>
      <div class="brand__sub">Automotive</div>
    </div>
    <div class="person">
      <div class="person__name">Lachie Westergaard</div>
      <div class="person__role">Director</div>
      <div class="person__address">48 Marlow Lane<br>Harlow Bay 3577</div>
    </div>
    <div class="divider"></div>
    <ul class="contact">
      <li><svg viewBox="0 0 10 10"><path d="M2 0.5 L3.6 0.5 L4.3 2.8 L3.2 3.6 Q4.2 5.8 6.4 6.8 L7.2 5.7 L9.5 6.4 L9.5 8 Q9.5 9.5 8 9.5 Q0.5 8.5 0.5 2 Q0.5 0.5 2 0.5Z"/></svg>07 842 1937</li>
      <li><svg viewBox="0 0 10 10"><path d="M2.5 0 H7.5 V10 H2.5Z M3.4 1.2 V8 H6.6 V1.2Z"/></svg>027 519 2764</li>
      <li><svg viewBox="0 0 10 10"><path d="M0 2 H10 V8 H0Z M0.8 2.6 L5 5.6 L9.2 2.6"/></svg>office@ridgebackmotors.co.nz</li>
      <li><svg viewBox="0 0 10 10"><circle cx="5" cy="5" r="4.8"/></svg>ridgebackmotors.co.nz</li>
    </ul>
  </section>

  <section class="card card--back" aria-label="Card back">
    <div class="brand">
      <div class="brand__name">Ridgeback Prime</div>
      <div class="brand__sub">Automotive</div>
    </div>
    <div class="appointment">APPOINTMENT</div>
    <div class="field-row">
      <div class="field">Date:<span class="field__line"></span></div>
      <div class="field">Time:<span class="field__line"></span></div>
    </div>
    <ul class="days">
      <li>Mon</li><li>Tue</li><li>Wed</li><li>Thur</li><li>Fri</li><li>Sat</li>
    </ul>
    <div class="services">
      <span>Vehicle Servicing</span><span>All Mechanical Repairs</span><span>Warrant of Fitness</span><br>
      <span>Tyres &amp; Wheel Alignments</span><span>Automotive Diagnostics</span><span>Automotive Parts &amp; Supplies</span>
    </div>
  </section>
</body>
</html>
```